Business Card for Fashion House

We need a business card design for our personalize fashion service for our customers. the business card should reflect reliability, luxury and creativity.
The brand Gravetto is extracted from "Graceful Vetto"; Gravetto provides fashion designs sprinkled with luxury and style tailored for our elite clients character profile.
Gravetto is created for those who embody class and elegance with a passion for style.
Target Market(s)
Affluent Customers
Industry/Entity Type
Fashion
Contact Information for Business Card
Rania Bou Khalil
Fashion Designer
Telephone: +971 5550123
Mobile +971 555987
Emal q@z.com
Website www.gravetto-example.com
Social Media Youtube g+ Facebook Instagram Pin /gravetto
Font styles to use
Other font styles liked:
- Audrey provided
Look and feel
Each slider illustrates characteristics of the customer's brand and the style your logo design should communicate.

```html
<!DOCTYPE html>
<html lang="en">
<head>
<meta charset="utf-8">
<title>Gravetto Business Card</title>
<link rel="stylesheet" href="https://fonts.googleapis.com/css2?family=Cormorant+Garamond:wght@400;500;600&family=Lato:wght@300;700&display=swap">
<style>
  :root {
    --stage: #d9d7d4;
    --ink-dark: #2e2a28;
    --band: #2b2929;
    --band-edge: #8c8a88;
    --paper: #f3f3f2;
    --ink: #1d1d1d;
    --muted: #4a4a4a;
    --light: #f4f1ee;
  }
  * { box-sizing: border-box; margin: 0; padding: 0; }
  html, body { width: 1200px; height: 1000px; overflow: hidden; }
  body {
    background: var(--stage);
    position: relative;
    font-family: "Cormorant Garamond", Georgia, serif;
  }
  .card {
    position: absolute;
    left: 220px;
    width: 760px;
    height: 434px;
    border-radius: 26px;
    overflow: hidden;
    box-shadow: 0 8px 22px rgba(0,0,0,.18);
  }
  .card--back { top: 44px; background: var(--ink-dark); }
  .card--front { top: 516px; background: var(--paper); }

  .brand {
    position: absolute;
    display: flex;
    align-items: center;
    gap: 22px;
    font-family: "Cormorant Garamond", Georgia, serif;
    font-weight: 500;
    text-transform: uppercase;
    letter-spacing: 0.38em;
  }
  .brand__mark { width: 22px; height: 22px; border: 2px solid currentColor; }
  .card--back .brand { color: var(--light); right: 70px; top: 250px; font-size: 34px; }
  .card--front .brand { color: var(--ink); left: 60px; top: 280px; font-size: 40px; }

  .divider {
    position: absolute; left: 430px; top: 92px;
    width: 2px; height: 160px; background: #6b6b6b;
  }

  .contact { position: absolute; left: 460px; top: 80px; color: var(--ink); }
  .contact__name {
    font-family: "Lato", Arial, sans-serif;
    font-size: 22px; font-weight: 300; text-transform: uppercase; letter-spacing: .01em;
  }
  .contact__name strong { font-weight: 700; }
  .contact__role { font-size: 17px; color: var(--muted); margin-top: -2px; }
  .contact__list { list-style: none; margin-top: 22px; }
  .contact__list li {
    display: flex; align-items: center; gap: 10px;
    font-size: 17px; line-height: 22px; color: var(--ink);
  }
  .contact__list svg { width: 14px; height: 14px; flex: none; }
  .contact__list .indent { padding-left: 24px; }

  .swoosh { position: absolute; inset: 0; width: 760px; height: 434px; }

  .social {
    position: absolute; left: 440px; top: 322px;
    display: flex; align-items: center; gap: 12px;
    transform: rotate(-13deg); transform-origin: left center;
    color: var(--light);
  }
  .social__dot { width: 18px; height: 18px; border-radius: 50%; background: var(--light); opacity: .9; }
  .social__handle { font-size: 20px; font-weight: 500; letter-spacing: .04em; margin-left: 4px; }
</style>
</head>
<body>

<section class="card card--back" aria-label="Card back">
  <div class="brand"><span class="brand__mark"></span>Gravetto</div>
</section>

<section class="card card--front" aria-label="Card front">
  <svg class="swoosh" viewBox="0 0 760 434" aria-hidden="true">
    <path d="M250 434 C 420 380, 560 270, 760 200 L 760 434 Z" fill="var(--band-edge)"/>
    <path d="M300 434 C 450 360, 580 290, 760 232 L 760 434 Z" fill="var(--band)"/>
  </svg>

  <div class="brand"><span class="brand__mark"></span>Gravetto</div>
  <div class="divider"></div>

  <div class="contact">
    <p class="contact__name">Rania Bou <strong>Khalil</strong></p>
    <p class="contact__role">Fashion Designer</p>
    <ul class="contact__list">
      <li>
        <svg viewBox="0 0 14 14"><rect x="3.5" y="1" width="7" height="12" rx="1.2" fill="none" stroke="currentColor" stroke-width="1.3"/></svg>
        +971 5550123
      </li>
      <li class="indent">+971 555987</li>
      <li>
        <svg viewBox="0 0 14 14"><path d="M3 1.5 L5.5 1.5 L6.5 4.5 L5 5.8 C5.8 7.6 6.6 8.4 8.2 9.2 L9.5 7.7 L12.5 8.7 L12.5 11.2 C12.5 12 11.8 12.6 11 12.5 C5.8 12 2 8.2 1.5 3 C1.4 2.2 2.1 1.5 3 1.5 Z" fill="currentColor"/></svg>
        www.gravetto-example.com
      </li>
      <li>
        <svg viewBox="0 0 14 14"><rect x="1" y="3" width="12" height="8.5" fill="none" stroke="currentColor" stroke-width="1.3"/><path d="M1 3 L7 8 L13 3" fill="none" stroke="currentColor" stroke-width="1.3"/></svg>
        q@z.com
      </li>
    </ul>
  </div>

  <div class="social">
    <span class="social__dot"></span>
    <span class="social__dot"></span>
    <span class="social__dot"></span>
    <span class="social__dot"></span>
    <span class="social__dot"></span>
    <span class="social__handle">/gravetto</span>
  </div>
</section>

</body>
</html>
```